RLB Stationary
CEO Business Card
RLB Stationary -
Use specific fonts
Use same logo font or complimentary fonts to logo
Professional
Dale Vorrinth
CEO
3187 Tollgate Fern Ct., #412 Brindle Falls, VA 20377
Dale@HollowbrookUpkeep.com
www.hollowbrookupkeep.com
We are a commercial construction company who's clients are premiere property management companies. Our presence should connote corporate strength and confidence. Our colors are gray and blue.
Services provided. General Facilities Management Build-Outs Carpentry Painting Drywall Ceramic Tile Masonry Concrete Tuck & Point Pavers Awnings Ceiling Tile Power Washing Graffiti Removal Doors & Windows Flood Remediation Apartment Turns & Much More

```html
<!DOCTYPE html>
<html lang="en">
<head>
<meta charset="utf-8">
<title>RLB – CEO Business Card</title>
<link rel="stylesheet" href="https://fonts.googleapis.com/css2?family=Arimo:wght@400;700&display=swap">
<style>
  :root {
    --page-bg: #e9e9ea;
    --card-white: #ffffff;
    --brand-navy: #1d3a6e;
    --brand-gray: #8a8c8f;
    --divider: #b9bcc2;
    --text-light: #ffffff;
  }
  html, body {
    margin: 0;
    padding: 0;
    width: 1200px;
    height: 780px;
    overflow: hidden;
    background: var(--page-bg);
    font-family: "Arimo", Arial, sans-serif;
  }
  .canvas {
    position: relative;
    width: 1200px;
    height: 780px;
  }
  .business-card {
    position: absolute;
    left: 120px;
    top: 110px;
    width: 960px;
    height: 560px;
    border-radius: 28px;
    overflow: hidden;
    display: flex;
    box-shadow: 0 10px 30px rgba(0,0,0,0.18);
  }
  .card-front-logo {
    width: 352px;
    background: var(--card-white);
    display: flex;
    align-items: center;
    justify-content: center;
    border-right: 4px solid var(--divider);
  }
  .brand-mark {
    display: flex;
    align-items: center;
    gap: 16px;
    margin-top: 40px;
  }
  .brand-square {
    width: 34px;
    height: 34px;
    background: var(--brand-gray);
  }
  .brand-name {
    font-weight: 700;
    font-size: 88px;
    letter-spacing: 1px;
    color: var(--brand-navy);
    line-height: 1;
  }
  .card-contact-panel {
    flex: 1;
    background: var(--brand-navy);
    color: var(--text-light);
    position: relative;
    text-align: right;
    padding: 34px 40px 0 0;
    box-sizing: border-box;
  }
  .person-name {
    font-weight: 700;
    font-size: 28px;
    margin: 0;
  }
  .person-title {
    font-size: 17px;
    margin: 8px 0 0;
  }
  .contact-details {
    position: absolute;
    right: 40px;
    top: 238px;
    font-size: 22px;
    line-height: 1.35;
  }
  .address {
    margin: 0 0 18px;
  }
  .contact-line {
    display: flex;
    justify-content: flex-end;
    align-items: center;
    gap: 14px;
    margin: 0 0 12px;
  }
  .contact-line svg {
    width: 20px;
    height: 20px;
    flex: none;
  }
</style>
</head>
<body>
<main class="canvas">
  <article class="business-card">
    <section class="card-front-logo">
      <div class="brand-mark">
        <span class="brand-square"></span>
        <span class="brand-name">RLB</span>
      </div>
    </section>
    <section class="card-contact-panel">
      <h1 class="person-name">Dale Vorrinth</h1>
      <p class="person-title">CEO</p>
      <div class="contact-details">
        <p class="address">3187 Tollgate Fern Ct., #412<br>Brindle Falls, VA 20377</p>
        <p class="contact-line">555.014.2283
          <svg viewBox="0 0 20 20" aria-hidden="true"><path d="M5 2h3l1.5 4-2 1.5a11 11 0 0 0 5 5l1.5-2 4 1.5v3a2 2 0 0 1-2 2A15 15 0 0 1 3 4a2 2 0 0 1 2-2z" fill="#fff"/></svg>
        </p>
        <p class="contact-line">555.017.6604
          <svg viewBox="0 0 20 20" aria-hidden="true"><rect x="4" y="2" width="10" height="6" fill="#fff"/><rect x="2" y="8" width="16" height="8" rx="1" fill="#fff"/><rect x="5" y="12" width="10" height="6" fill="#fff" stroke="#1d3a6e" stroke-width="1"/></svg>
        </p>
        <p class="contact-line">Dale@HollowbrookUpkeep.com
          <svg viewBox="0 0 20 20" aria-hidden="true"><text x="10" y="16" text-anchor="middle" font-family="Arimo, Arial, sans-serif" font-weight="700" font-size="18" fill="#fff">@</text></svg>
        </p>
        <p class="contact-line">www.hollowbrookupkeep.com
          <svg viewBox="0 0 20 20" aria-hidden="true"><circle cx="10" cy="10" r="8" fill="none" stroke="#fff" stroke-width="1.6"/><ellipse cx="10" cy="10" rx="3.5" ry="8" fill="none" stroke="#fff" stroke-width="1.4"/><line x1="2" y1="10" x2="18" y2="10" stroke="#fff" stroke-width="1.4"/></svg>
        </p>
      </div>
    </section>
  </article>
</main>
</body>
</html>
```